Need a flyer overhaul and minor changes

flyer is 5.5" x 8.5" we need to change the $250.00 to $325.00, update our company logo on the brochure, and also have an area where we can have the store address (318 W Harlan Ave, Del Rio, TX 78840 - (830) 642-9158). I've attached a our current brochure and our updated logo and we just want to make look better and updated.

Industry/Entity Type

Lending and Finance

Requirements
Nice to have
• updated layout and pictures

```html
<!DOCTYPE html>
<html lang="en">
<head>
<meta charset="utf-8">
<title>Keystone Lending Group – Title Loan Flyer</title>
<link rel="stylesheet" href="https://fonts.googleapis.com/css2?family=Catamaran:wght@300;400;700;800&family=Montserrat:wght@700;800&family=Roboto+Condensed:wght@700&family=Roboto:wght@500;700&display=swap">
<style>
  :root {
    --red: #ec1c24;
    --green: #0c5a2c;
    --white: #ffffff;
    --ink: #0c4a24;
    --yellow: #fde65a;
    --blush: #f6d9d6;
  }
  * { margin: 0; padding: 0; box-sizing: border-box; }
  html, body { width: 776px; height: 1200px; overflow: hidden; background: var(--white); }
  .flyer { position: relative; width: 776px; height: 1200px; overflow: hidden; font-family: "Catamaran", sans-serif; background: var(--white); }

  .top-wash { position: absolute; left: 0; top: 0; width: 776px; height: 141px; background: linear-gradient(180deg, #ffffff 0%, #ffffff 35%, var(--blush) 100%); }
  .brand { position: absolute; display: flex; align-items: center; gap: 8px; color: var(--green); font-family: "Catamaran", sans-serif; font-weight: 700; white-space: nowrap; }
  .brand-dot { border-radius: 50%; background: var(--green); flex: none; }
  .brand-top { left: 0; width: 776px; top: 44px; justify-content: center; font-size: 38px; line-height: 1; }
  .brand-top .brand-dot { width: 26px; height: 26px; }
  .brand-bottom { left: 498px; width: 170px; top: 990px; justify-content: center; font-size: 24px; line-height: 1.05; white-space: normal; text-align: left; }
  .brand-bottom .brand-dot { width: 18px; height: 18px; }

  .headline-band { position: absolute; left: 0; top: 141px; width: 776px; height: 102px; background: var(--red); color: var(--white); display: flex; align-items: center; justify-content: center; gap: 14px; font-size: 60px; line-height: 1; }
  .headline-band .light { font-weight: 300; }
  .headline-band .bold { font-weight: 800; }

  .glow { position: absolute; left: 0; top: 320px; width: 776px; height: 420px; background: linear-gradient(90deg, var(--yellow) 0%, #fff3a8 30%, #ffffff 55%); }
  .glow::after { content: ""; position: absolute; inset: 0; background: linear-gradient(180deg, rgba(255,255,255,0) 60%, #ffffff 100%); }

  .compare-pill { position: absolute; left: 26px; top: 254px; width: 724px; height: 66px; background: var(--green); border-radius: 26px 6px 26px 6px; color: var(--white); font-family: "Montserrat", sans-serif; font-weight: 800; font-size: 41px; letter-spacing: 1.5px; display: flex; align-items: center; justify-content: center; }

  .photo { position: absolute; left: 0; top: 330px; width: 420px; height: 733px; background: radial-gradient(ellipse at 45% 35%, #c59a82 0%, #b88a72 22%, rgba(200,215,225,0.95) 48%, rgba(214,226,234,0.6) 75%, rgba(255,255,255,0) 100%); }

  .loan-table { position: absolute; left: 335px; top: 330px; width: 429px; height: 460px; background: var(--white); }
  .table-head { height: 51px; border: 2px solid var(--green); display: flex; align-items: center; justify-content: center; font-family: "Roboto Condensed", sans-serif; font-weight: 700; font-size: 40px; color: var(--green); letter-spacing: -0.5px; }
  .table-cols { display: flex; justify-content: space-between; margin-top: 0; }
  .col { display: flex; width: 201px; }
  .col-right { width: 203px; }
  .col-nums { width: 45px; background: var(--green); padding-top: 10px; padding-bottom: 6px; }
  .col-vals { flex: 1; padding-top: 10px; padding-left: 2px; }
  .row { height: 32.9px; display: flex; align-items: center; }
  .col-nums .row { justify-content: center; color: var(--white); font-family: "Roboto", sans-serif; font-weight: 500; font-size: 19px; }
  .col-vals .row { padding-left: 18px; font-family: "Roboto", sans-serif; font-weight: 700; font-size: 24px; color: var(--ink); }
  .col-right .col-vals .row { padding-left: 20px; }
  .col-vals .row.shade { background: var(--green); color: var(--white); height: 31px; margin-bottom: 1.9px; }
  .col-vals .row.plain { margin-bottom: 0; }

  .result-box { position: absolute; left: 342px; top: 800px; width: 424px; height: 92px; border: 2px solid var(--red); border-left: none; background: var(--white); }
  .paid { position: absolute; left: 8px; top: 4px; font-family: "Montserrat", sans-serif; font-weight: 800; font-size: 34px; color: var(--green); letter-spacing: -1px; }
  .owe { position: absolute; right: 8px; top: 4px; text-align: right; font-family: "Catamaran", sans-serif; font-weight: 800; font-size: 37px; line-height: 0.98; color: var(--red); }
  .owe .amount { display: block; padding-right: 34px; font-size: 42px; }

  .spanish-pill { position: absolute; left: 406px; top: 905px; width: 370px; height: 53px; background: var(--green); border-radius: 22px 0 0 6px; color: var(--white); font-family: "Montserrat", sans-serif; font-weight: 700; font-size: 25px; letter-spacing: 2px; display: flex; align-items: center; justify-content: center; }

  .visit-band { position: absolute; left: 0; top: 1063px; width: 776px; height: 80px; background: var(--red); display: flex; align-items: center; justify-content: center; }
  .visit-label { background: var(--white); color: var(--red); font-family: "Catamaran", sans-serif; font-weight: 700; font-size: 28px; height: 38px; padding: 0 4px 0 8px; display: flex; align-items: center; letter-spacing: -0.3px; }
  .visit-arrow { width: 18px; height: 38px; display: block; }
  .visit-url { color: var(--white); font-family: "Catamaran", sans-serif; font-weight: 800; font-size: 35px; margin-left: 6px; letter-spacing: 0.2px; }

  .address-band { position: absolute; left: 0; top: 1143px; width: 776px; height: 57px; background: var(--green); }
  .address-box { position: absolute; left: 17px; top: 10px; width: 745px; height: 37px; background: var(--white); display: flex; align-items: center; padding-left: 34px; gap: 10px; font-family: "Catamaran", sans-serif; font-weight: 700; font-size: 26px; color: var(--green); white-space: nowrap; }
  .pin { width: 17px; height: 24px; flex: none; }
</style>
</head>
<body>
<main class="flyer">
  <div class="top-wash"></div>
  <div class="brand brand-top"><span class="brand-dot"></span>Keystone Lending Group</div>

  <header class="headline-band">
    <span class="light">Stuck in a</span>
    <span class="bold">Title Loan?</span>
  </header>

  <div class="glow"></div>
  <div class="photo" role="img" aria-label="Photo of a smiling woman holding a fan of cash"></div>

  <div class="compare-pill">$1,000 LOAN COMPARISON</div>

  <section class="loan-table" aria-label="Twelve-payment comparison">
    <div class="table-head">TITLE LOAN</div>
    <div class="table-cols">
      <div class="col col-left">
        <div class="col-nums">
          <div class="row">1</div><div class="row">2</div><div class="row">3</div><div class="row">4</div>
          <div class="row">5</div><div class="row">6</div><div class="row">7</div><div class="row">8</div>
          <div class="row">9</div><div class="row">10</div><div class="row">11</div><div class="row">12</div>
        </div>
        <div class="col-vals">
          <div class="row shade">$131.67</div><div class="row plain">$131.67</div>
          <div class="row shade">$131.67</div><div class="row plain">$131.67</div>
          <div class="row shade">$131.67</div><div class="row plain">$131.67</div>
          <div class="row shade">$131.67</div><div class="row plain">$131.67</div>
          <div class="row shade">$131.67</div><div class="row plain">$131.67</div>
          <div class="row shade">$131.67</div><div class="row plain">$131.67</div>
        </div>
      </div>
      <div class="col col-right">
        <div class="col-nums">
          <div class="row">1</div><div class="row">2</div><div class="row">3</div><div class="row">4</div>
          <div class="row">5</div><div class="row">6</div><div class="row">7</div><div class="row">8</div>
          <div class="row">9</div><div class="row">10</div><div class="row">11</div><div class="row">12</div>
        </div>
        <div class="col-vals">
          <div class="row shade">$325.00</div><div class="row plain">$325.00</div>
          <div class="row shade">$325.00</div><div class="row plain">$325.00</div>
          <div class="row shade">$325.00</div><div class="row plain">$325.00</div>
          <div class="row shade">$325.00</div><div class="row plain">$325.00</div>
          <div class="row shade">$325.00</div><div class="row plain">$325.00</div>
          <div class="row shade">$325.00</div><div class="row plain">$325.00</div>
        </div>
      </div>
    </div>
  </section>

  <div class="result-box">
    <div class="paid">PAID OFF</div>
    <div class="owe">STILL OWE<span class="amount">$1,000</span></div>
  </div>

  <div class="spanish-pill">SE HABLA ESPAÑOL</div>

  <div class="brand brand-bottom"><span class="brand-dot"></span>Keystone Lending Group</div>

  <div class="visit-band">
    <span class="visit-label">VISIT US AT</span>
    <svg class="visit-arrow" viewBox="0 0 18 38" aria-hidden="true"><polygon points="0,0 18,19 0,38" fill="#ffffff"/></svg>
    <span class="visit-url">KEYSTONELEND.COM</span>
  </div>

  <footer class="address-band">
    <div class="address-box">
      <svg class="pin" viewBox="0 0 17 24" aria-hidden="true"><path d="M8.5 0C3.8 0 0 3.7 0 8.3 0 14.5 8.5 24 8.5 24S17 14.5 17 8.3C17 3.7 13.2 0 8.5 0zm0 11.6a3.3 3.3 0 1 1 0-6.6 3.3 3.3 0 0 1 0 6.6z" fill="#0c5a2c"/></svg>
      <span>318 W Harlan Ave, Del Rio, TX 78840 - (830) 642-9158</span>
    </div>
  </footer>
</main>
</body>
</html>
```